GPS Tracker Business Card Design

We need a business card for a GPS Vehicle tracking company. We sell the hardware for the vehicle and the software platform to monitor your vehicle/s. Including high asset non-powered vehicles like a trailer using our solar powered unit.
We like using dark blue to different shades of blue along with gold. We have phone apps for Android and Apple devices.

We have a platform for families wanting to track their teenage driver and children; Plus a Fleet vehicle tracking platform.

Features: unlimited number of vehicles and/or assets including snow mobiles forklifts generators trailers airport equipment

Reports for driving behavior reports and alerts dashboard fleet maintenace timeline view and replay geofence real time alerts logbook scheduling route optimization accounting integration fleet grouping closest vehicle locator On Board Diagnostics.

Benefits: Increased productivity improved fuel efficiency organizing your business improve time management simplify back end processes, reduce fleet fuel efficiency and expenses increase fleet security etc..

Please view website: Velmora.com

Industry/Entity Type

Business

Contact Information for Business Card

Harold B Pennick

```html
<!DOCTYPE html>
<html lang="en">
<head>
<meta charset="utf-8">
<title>Velmora Business Card</title>
<link href="https://fonts.googleapis.com/css2?family=Oswald:wght@600&family=Open+Sans:wght@400;600&display=swap" rel="stylesheet">
<style>
  :root {
    --stage: #000000;
    --card: #ffffff;
    --ink: #111111;
    --rule: #8a8a8a;
  }
  html, body {
    margin: 0;
    padding: 0;
    width: 1200px;
    height: 900px;
    overflow: hidden;
    background: var(--stage);
  }
  .canvas {
    position: relative;
    width: 1200px;
    height: 900px;
    background: var(--stage);
  }
  .card {
    position: absolute;
    top: 275px;
    width: 477px;
    height: 293px;
    background: var(--card);
    overflow: hidden;
  }
  .card--front {
    left: 116px;
    border-radius: 0 56px 0 56px;
  }
  .card--back {
    left: 622px;
    border-radius: 56px 0 56px 0;
  }
  .brand-name {
    position: absolute;
    left: 0;
    width: 100%;
    text-align: center;
    font-family: "Oswald", sans-serif;
    font-weight: 600;
    color: var(--ink);
    letter-spacing: 1px;
    line-height: 1;
  }
  .card--front .brand-name {
    top: 62px;
    font-size: 64px;
  }
  .card--back .brand-name {
    top: 108px;
    font-size: 72px;
  }
  .holder {
    position: absolute;
    top: 203px;
    left: 0;
    width: 100%;
    display: flex;
    align-items: center;
    gap: 12px;
  }
  .holder__rule {
    flex: 1;
    height: 1px;
    background: var(--rule);
  }
  .holder__name {
    font-family: "Open Sans", sans-serif;
    font-weight: 600;
    font-size: 16px;
    color: var(--ink);
  }
  .web {
    position: absolute;
    top: 239px;
    left: 0;
    width: 100%;
    display: flex;
    justify-content: center;
    align-items: center;
    gap: 5px;
    font-family: "Open Sans", sans-serif;
    font-size: 12.5px;
    color: var(--ink);
  }
  .web__icon {
    width: 10px;
    height: 10px;
  }
</style>
</head>
<body>
  <main class="canvas">
    <section class="card card--front">
      <div class="brand-name">Velmora</div>
      <div class="holder">
        <span class="holder__rule"></span>
        <span class="holder__name">Harold B Pennick</span>
        <span class="holder__rule"></span>
      </div>
      <div class="web">
        <svg class="web__icon" viewBox="0 0 10 10" aria-hidden="true">
          <circle cx="5" cy="5" r="4.6" fill="var(--ink)"/>
          <path d="M2.5 3.2 Q4 2.4 4.8 3.6 Q4 5 5.6 5.6 Q5.8 7.4 4.6 8.4 Q3.2 6.8 2.5 5.2 Z" fill="var(--card)"/>
        </svg>
        <span class="web__url">www.velmora.com</span>
      </div>
    </section>
    <section class="card card--back">
      <div class="brand-name">Velmora</div>
    </section>
  </main>
</body>
</html>
```